Harrow Collective
Chartered accountants & business advisors company seeks logo & business card design refresh - Financial Services
Simple
Derek Ostrander
Senior Project Accountant
PO Box 27 458 Wellington 6571
derek@harrowcollective.example.nz
harrowcollective.example.nz
Full Bleed Size (starting document size) 94 x 58 mm 1110 x 685 pixels * Finished artwork should use the full bleed dimensions for best results. Document Trim Size (final size after being cut) 91 x 55 mm 1075 x 650 pixels * Please be sure to keep all text within the safe margin. Resolution 300 DPI
Simple, perhaps solid colour with the web address (and logo etc)

```html
<!DOCTYPE html>
<html lang="en">
<head>
<meta charset="utf-8">
<title>Harrow Collective – Business Card</title>
<link rel="stylesheet" href="https://fonts.googleapis.com/css2?family=Cinzel:wght@500&family=Open+Sans:wght@400;600&display=swap">
<style>
  :root {
    --bg: #d9dadb;
    --brand-blue: #3a7fd0;
    --accent-red: #c62a2f;
    --ink: #1f2024;
    --card-dark: #1d1d1f;
    --tab-grey: #8c8d90;
    --paper: #ffffff;
    --muted-light: #c9cbd0;
    --line-white: rgba(255,255,255,0.85);
  }
  * { box-sizing: border-box; margin: 0; padding: 0; }
  html, body { width: 1200px; height: 895px; overflow: hidden; }
  body {
    background: var(--bg);
    font-family: "Open Sans", Arial, sans-serif;
    position: relative;
  }
  .card {
    position: absolute;
    left: 270px;
    width: 660px;
    height: 399px;
    overflow: hidden;
    box-shadow: 0 6px 18px rgba(0,0,0,0.18);
  }
  .card--front { top: 32px; background: var(--paper); }
  .card--back { top: 464px; background: var(--card-dark); }

  .tab {
    position: absolute;
    right: 0;
    width: 150px;
    height: 58px;
    background: var(--tab-grey);
    clip-path: polygon(22% 0, 100% 0, 100% 100%, 0 100%);
  }
  .card--front .tab { top: 104px; }
  .card--back .tab { top: 62px; }

  .wordmark {
    position: absolute;
    display: flex;
    align-items: center;
    gap: 12px;
  }
  .wordmark__dot {
    width: 20px; height: 20px;
    border-radius: 50%;
    background: var(--brand-blue);
    flex: none;
  }
  .wordmark__name {
    font-family: "Cinzel", Georgia, serif;
    font-weight: 500;
    color: var(--brand-blue);
    letter-spacing: 1px;
    white-space: nowrap;
  }
  .card--front .wordmark { left: 40px; top: 46px; }
  .card--front .wordmark__name { font-size: 30px; }
  .card--back .wordmark { left: 52px; top: 150px; }
  .card--back .wordmark__name { font-size: 36px; }

  .back-web {
    position: absolute;
    left: 86px;
    top: 212px;
    font-size: 14px;
    letter-spacing: 1px;
    color: var(--muted-light);
  }

  .person {
    position: absolute;
    right: 30px;
    top: 172px;
    width: 250px;
  }
  .person__name {
    font-size: 17px;
    font-weight: 600;
    letter-spacing: 0.5px;
    text-transform: uppercase;
    color: var(--ink);
    white-space: nowrap;
  }
  .person__first { color: var(--accent-red); }
  .person__title {
    font-size: 10px;
    letter-spacing: 0.8px;
    text-transform: uppercase;
    color: var(--ink);
    margin-top: 2px;
    white-space: nowrap;
  }

  .contact-panel {
    position: absolute;
    left: 24px;
    right: 24px;
    top: 228px;
    bottom: 22px;
    background: var(--brand-blue);
    border-radius: 12px;
    display: grid;
    grid-template-columns: 1fr 1.3fr 1fr;
    color: #fff;
  }
  .contact-panel__col {
    display: flex;
    flex-direction: column;
    align-items: center;
    justify-content: flex-start;
    padding: 20px 10px 10px;
    text-align: center;
    font-size: 12px;
    line-height: 1.6;
  }
  .contact-panel__col + .contact-panel__col { border-left: 1px solid var(--line-white); }
  .contact-panel__icon { width: 30px; height: 30px; margin-bottom: 14px; }
</style>
</head>
<body>

<section class="card card--front" aria-label="Business card front">
  <div class="wordmark">
    <span class="wordmark__dot"></span>
    <span class="wordmark__name">Harrow Collective</span>
  </div>
  <div class="tab"></div>
  <div class="person">
    <p class="person__name"><span class="person__first">Derek</span> Ostrander</p>
    <p class="person__title">Senior Project Accountant</p>
  </div>
  <div class="contact-panel">
    <div class="contact-panel__col">
      <svg class="contact-panel__icon" viewBox="0 0 24 24" aria-hidden="true">
        <path fill="#fff" d="M6.6 10.8a15.1 15.1 0 0 0 6.6 6.6l2.2-2.2a1 1 0 0 1 1-.25 11.4 11.4 0 0 0 3.6.57 1 1 0 0 1 1 1V20a1 1 0 0 1-1 1A17 17 0 0 1 3 4a1 1 0 0 1 1-1h3.5a1 1 0 0 1 1 1c0 1.250.2 2.45.57 3.57a1 1 0 0 1-.25 1z"/>
      </svg>
      <span>04 555 0182</span>
      <span>04 555 0193</span>
    </div>
    <div class="contact-panel__col">
      <svg class="contact-panel__icon" viewBox="0 0 24 24" aria-hidden="true">
        <g fill="none" stroke="#fff" stroke-width="1.6">
          <circle cx="12" cy="12" r="9.5"/>
          <ellipse cx="12" cy="12" rx="4.2" ry="9.5"/>
          <path d="M2.5 12h19M4 7h16M4 17h16"/>
        </g>
      </svg>
      <span>derek@harrowcollective.example.nz</span>
      <span>harrowcollective.example.nz</span>
    </div>
    <div class="contact-panel__col">
      <svg class="contact-panel__icon" viewBox="0 0 24 24" aria-hidden="true">
        <path fill="#fff" d="M12 2a7 7 0 0 0-7 7c0 5.2 7 13 7 13s7-7.8 7-13a7 7 0 0 0-7-7zm0 9.5A2.5 2.5 0 1 1 12 6.5a2.5 2.5 0 0 1 0 5z"/>
      </svg>
      <span>PO Box 27 458</span>
      <span>Wellington 6571</span>
    </div>
  </div>
</section>

<section class="card card--back" aria-label="Business card back">
  <div class="tab"></div>
  <div class="wordmark">
    <span class="wordmark__dot"></span>
    <span class="wordmark__name">Harrow Collective</span>
  </div>
  <p class="back-web">harrowcollective.example.nz</p>
</section>

</body>
</html>
```